Dog grooming business card
This is a business card for m dog grooming business like it say above.
In the priorities box below I will have the text that I want on the card.

Industry/Entity Type

Business

Colors

Designer to choose colors to be used in the design.

Requirements
Must have
• My logo and the insurance stamp must be on the card.

Text it must have :

Professional grooming services
Email: lindomerfield@brightmail.example
Text or call 1 705 318 6052
KSR certified/member
Pet first aid certified
Next appointment ___________________________________
Nice to have
• Greens to match my logo

```html
<!DOCTYPE html>
<html lang="en">
<head>
<meta charset="utf-8">
<title>Lindo Merfield – Business Card</title>
<link rel="stylesheet" href="https://fonts.googleapis.com/css2?family=Roboto:wght@300;400&display=swap">
<style>
  :root {
    --bg: #d8dae1;
    --ink: #221f20;
    --green: #9bc53a;
    --paper: #e6e6e6;
    --light-text: #e9e9e9;
    --dark-text: #221f20;
    --badge: #ffffff;
  }
  * { margin: 0; padding: 0; box-sizing: border-box; }
  html, body {
    width: 1200px; height: 900px; overflow: hidden;
    background: var(--bg);
    font-family: "Roboto", Arial, sans-serif;
  }
  .stage {
    width: 1200px; height: 900px;
    display: flex; align-items: center; justify-content: center; gap: 60px;
  }
  .card {
    width: 500px; height: 286px;
    border-radius: 30px; overflow: hidden;
    display: flex; flex-direction: column;
  }
  /* front */
  .front__top {
    height: 141px; background: var(--ink);
    display: flex; flex-direction: column; align-items: center; justify-content: flex-end;
    padding-bottom: 6px;
  }
  .logo {
    display: flex; align-items: center; gap: 8px;
    color: var(--green); font-weight: 400; font-size: 26px;
    margin-bottom: 14px;
  }
  .logo__dot { width: 16px; height: 16px; border-radius: 50%; background: var(--green); }
  .tagline { color: var(--light-text); font-weight: 300; font-size: 22px; letter-spacing: 0.2px; }
  .front__bottom {
    flex: 1; background: var(--green);
    display: flex; flex-direction: column; align-items: center; padding-top: 11px;
  }
  .badge {
    width: 84px; height: 44px; background: var(--badge);
    border-radius: 7px; border: 1px solid #b9b9b9; margin-bottom: 10px;
  }
  .contact {
    display: flex; align-items: center; gap: 8px;
    color: var(--dark-text); font-size: 17px; font-weight: 400; line-height: 28px;
  }
  .contact svg { width: 21px; height: 16px; fill: var(--dark-text); }
  /* back */
  .back__top {
    height: 120px; background: var(--ink);
    display: flex; align-items: center; justify-content: space-between;
    padding: 0 34px 0 48px;
  }
  .back__tagline { color: var(--light-text); font-weight: 300; font-size: 26px; line-height: 30px; max-width: 270px; }
  .back__top .logo { margin: 40px 0 0; font-size: 20px; }
  .back__bottom {
    flex: 1; background: var(--paper);
    padding: 24px 48px; color: var(--dark-text);
    font-weight: 300; font-size: 21px; line-height: 29px;
  }
</style>
</head>
<body>
<main class="stage">
  <section class="card card--front">
    <div class="front__top">
      <div class="logo"><span class="logo__dot"></span>Lindo Merfield</div>
      <p class="tagline">Professional grooming services</p>
    </div>
    <div class="front__bottom">
      <div class="badge" role="img" aria-label="Insurance protection stamp"></div>
      <p class="contact">
        <svg viewBox="0 0 24 18" aria-hidden="true"><path d="M2 6c0-3 5-5 10-5s10 2 10 5v2h-6V6H8v2H2z"/><path d="M6 9h12l3 8H3z"/></svg>
        1 705 318 6052
      </p>
      <p class="contact">
        <svg viewBox="0 0 24 18" aria-hidden="true"><path d="M1 1h22v2L12 10 1 3z"/><path d="M1 5l11 7 11-7v12H1z"/></svg>
        lindomerfield@brightmail.example
      </p>
    </div>
  </section>

  <section class="card card--back">
    <div class="back__top">
      <p class="back__tagline">Professional grooming services</p>
      <div class="logo"><span class="logo__dot"></span>Lindo Merfield</div>
    </div>
    <div class="back__bottom">
      <p>KSR certified/member</p>
      <p>Pet first aid certified</p>
      <p>Next appointment</p>
    </div>
  </section>
</main>
</body>
</html>
```